CrewLedger business cards

Software for fire departments

Target Market(s)

Fire Departments

Industry/Entity Type

Business

Contact Information for Business Card

see attachments. Looking to print three sets of cards.

Requirements
Must have
• front and back
Nice to have
• rounded corners

```html
<!DOCTYPE html>
<html lang="en">
<head>
<meta charset="utf-8">
<title>CrewLedger business cards</title>
<link href="https://fonts.googleapis.com/css2?family=Noto+Serif:wght@400;700&display=swap" rel="stylesheet">
<style>
  :root {
    --canvas: #ecebe8;
    --card-white: #ffffff;
    --brand-red: #b3151c;
    --brand-red-light: #d8454b;
    --brand-red-dark: #8f0d13;
    --ink: #2a2a2a;
    --shadow: rgba(0, 0, 0, 0.18);
  }
  * { box-sizing: border-box; margin: 0; padding: 0; }
  html, body {
    width: 1200px;
    height: 913px;
    overflow: hidden;
    background: var(--canvas);
    font-family: "Noto Serif", Georgia, serif;
  }
  .canvas {
    position: relative;
    width: 1200px;
    height: 913px;
  }
  .card {
    position: absolute;
    top: 313px;
    width: 500px;
    height: 286px;
    border-radius: 20px;
    background: var(--card-white);
    overflow: hidden;
    box-shadow: 0 8px 24px var(--shadow);
  }
  .card--front { left: 70px; }
  .card--back { left: 630px; }

  /* Front */
  .front-content {
    position: absolute;
    inset: 0;
    display: flex;
    flex-direction: column;
    align-items: center;
    justify-content: center;
    text-align: center;
  }
  .brand-name {
    font-size: 50px;
    font-weight: 700;
    color: var(--brand-red);
    letter-spacing: 0.5px;
    line-height: 1;
  }
  .tagline {
    margin-top: 34px;
    font-size: 17px;
    font-weight: 700;
    color: var(--ink);
  }
  .website {
    margin-top: 10px;
    font-size: 12px;
    color: var(--brand-red);
  }

  /* Back */
  .red-band {
    position: absolute;
    inset: 0;
    width: 100%;
    height: 100%;
  }
  .person {
    position: absolute;
    top: 40px;
    left: 0;
    right: 0;
    text-align: center;
    color: var(--brand-red);
  }
  .person-name {
    font-size: 18px;
    font-weight: 700;
  }
  .person-role {
    margin-top: 2px;
    font-size: 17px;
  }
  .contact {
    position: absolute;
    top: 148px;
    left: 0;
    right: 0;
    text-align: center;
    color: #ffffff;
    font-size: 15px;
    line-height: 1.4;
  }
  .contact-email {
    margin-top: 12px;
    font-size: 18px;
  }
</style>
</head>
<body>
<main class="canvas">

  <section class="card card--front" aria-label="Card front">
    <div class="front-content">
      <div class="brand-name">CrewLedger</div>
      <p class="tagline">Smart Risk Management for Fire Services</p>
      <p class="website">www.crewledger.com</p>
    </div>
  </section>

  <section class="card card--back" aria-label="Card back">
    <svg class="red-band" viewBox="0 0 500 286" preserveAspectRatio="none" aria-hidden="true">
      <defs>
        <linearGradient id="bandGradient" x1="0" y1="1" x2="1" y2="0">
          <stop offset="0" stop-color="var(--brand-red-dark)"/>
          <stop offset="0.55" stop-color="var(--brand-red)"/>
          <stop offset="1" stop-color="var(--brand-red-light)"/>
        </linearGradient>
      </defs>
      <polygon points="0,170 500,110 500,286 0,286" fill="url(#bandGradient)"/>
    </svg>
    <div class="person">
      <p class="person-name">Dan Whitford</p>
      <p class="person-role">Training + Business Development</p>
    </div>
    <div class="contact">
      <p>978-555-0142</p>
      <p>14 Harbor Mill Road</p>
      <p>Northfield, MA 01360</p>
      <p class="contact-email">dan.whitford@crewledger.com</p>
    </div>
  </section>

</main>
</body>
</html>
```